cutest and professional business cards

I am looking at getting very good designs that will scream - contact this TEAM (7)
So could be that one or two awesome design and in variations for members of my team. Vector files are attached within the brief.
I will like the circle image (see vector-file) to be within the back of the cards as part of the design and the text "You're Creative - Join our Community"

Target Market(s)

Creative youths and millennials as well as very business/entrepreneurial minded community.

Contact Information for Business Card

logo,
name: for design1: Marlene Ikpefa for design2,3,4,5,6,7: leave blank space to possibility to handprint/sign name
position: design1: Founder, design2,3,4,5,6,7: community relationship manager, Fullstack developer, software designer, digital marketer, financial and operating officer, creative intern
address: Tendrilhub - 42 Wexmoor Ave Nepean ON k4r 3x2
number: 613-4289-517
website: www.fyrolume.com
linkedin -/fyrolum
facebook - /fyrolum
twitter - /fyrolu
instagram -/fyrolum

Font styles to use
Other font styles liked:
• monserratt

Requirements
Must have
• Font type: monserratt
• colours: off blue #1BBC9C , Red #BB2838
Nice to have
• a catchy, youthful and professional design
Should not have
• any additional colors besides dark grey and white.

```html
<!DOCTYPE html>
<html lang="en">
<head>
<meta charset="utf-8">
<title>Fyrolume business cards</title>
<link rel="stylesheet" href="https://fonts.googleapis.com/css2?family=Montserrat:wght@300;400;500;700&display=swap">
<style>
  :root {
    --teal: #1BBC9C;
    --red: #BB2838;
    --ink: #2f2f2f;
    --band: #2b2b2b;
    --paper: #ffffff;
    --backdrop: #e9ebeb;
    --mint-soft: #d3f0ea;
    --rose-soft: #f3d4d7;
  }
  * { box-sizing: border-box; margin: 0; padding: 0; }
  html, body {
    width: 1200px; height: 900px; overflow: hidden;
    background: var(--backdrop);
    font-family: "Montserrat", sans-serif;
    color: var(--ink);
  }
  .sheet { position: relative; width: 1200px; height: 900px; }
  .card {
    position: absolute; left: 250px; width: 700px; height: 400px;
    background: var(--paper);
    box-shadow: 0 6px 18px rgba(0,0,0,0.10);
    overflow: hidden;
  }
  .card--front { top: 30px; }
  .card--back { top: 470px; }

  /* front */
  .hands-art {
    position: absolute; left: -20px; top: 90px; width: 330px; height: 330px;
    border-radius: 50% 50% 0 50%;
    background: linear-gradient(160deg, var(--mint-soft) 0%, var(--mint-soft) 45%, var(--rose-soft) 60%, var(--rose-soft) 100%);
  }
  .brand { display: flex; align-items: center; gap: 12px; }
  .brand__dot { border-radius: 50%; background: var(--teal); flex: none; }
  .brand__name { font-weight: 700; color: var(--ink); line-height: 1; letter-spacing: -0.5px; }
  .card--front .brand { position: absolute; left: 300px; top: 130px; }
  .card--front .brand__dot { width: 44px; height: 44px; }
  .card--front .brand__name { font-size: 60px; }
  .front-tagline {
    position: absolute; left: 356px; top: 202px;
    font-size: 20px; font-weight: 500; color: var(--ink);
  }
  .front-url {
    position: absolute; left: 358px; top: 240px;
    font-size: 13px; font-weight: 400; letter-spacing: 6px; color: var(--ink);
  }

  /* back */
  .card--back .brand { position: absolute; left: 46px; top: 38px; gap: 8px; }
  .card--back .brand__dot { width: 26px; height: 26px; }
  .card--back .brand__name { font-size: 34px; }
  .back-tagline {
    position: absolute; left: 82px; top: 78px;
    font-size: 11px; font-weight: 500;
  }
  .person { position: absolute; left: 46px; top: 128px; }
  .person__name { font-size: 28px; font-weight: 700; letter-spacing: -0.3px; }
  .person__roles {
    margin-top: 6px; width: 400px;
    font-size: 12px; font-weight: 300; line-height: 1.45;
  }
  .contact-line { display: flex; align-items: flex-start; gap: 8px; font-size: 13px; font-weight: 300; line-height: 1.4; }
  .contact-line svg { flex: none; margin-top: 3px; }
  .address { position: absolute; left: 46px; top: 240px; }
  .reach { position: absolute; left: 470px; top: 180px; display: flex; flex-direction: column; gap: 4px; }
  .social-band {
    position: absolute; left: 0; right: 0; top: 318px; height: 52px;
    background: var(--band);
    display: flex; align-items: center; justify-content: space-around;
    padding: 0 30px;
  }
  .social-item { display: flex; align-items: center; gap: 8px; color: var(--teal); font-size: 13px; font-weight: 400; }
  .social-item__mark { width: 10px; height: 10px; background: var(--teal); }
</style>
</head>
<body>
<main class="sheet">

  <section class="card card--front" aria-label="Card front">
    <div class="hands-art" role="img" aria-label="Soft illustration of two open hands in mint and pink"></div>
    <div class="brand">
      <span class="brand__dot"></span>
      <span class="brand__name">Fyrolume</span>
    </div>
    <p class="front-tagline">Makers power Commerce</p>
    <p class="front-url">www.fyrolume.com</p>
  </section>

  <section class="card card--back" aria-label="Card back">
    <div class="brand">
      <span class="brand__dot"></span>
      <span class="brand__name">Fyrolume</span>
    </div>
    <p class="back-tagline">Makers power Commerce</p>

    <div class="person">
      <h1 class="person__name">Marlene Ikpefa</h1>
      <p class="person__roles">community relationship manager, Fullstack developer, software designer, digital marketer, financial and operating officer, creative intern</p>
    </div>

    <div class="address contact-line">
      <svg width="12" height="12" viewBox="0 0 12 12" aria-hidden="true"><path d="M1 6 L6 1.5 L11 6 M2.5 5 V10.5 H9.5 V5" fill="none" stroke="var(--teal)" stroke-width="1.5"/></svg>
      <span>Tendrilhub - 42 Wexmoor<br>Ave Nepean ON k4r 3x2</span>
    </div>

    <div class="reach">
      <div class="contact-line">
        <svg width="10" height="12" viewBox="0 0 10 12" aria-hidden="true"><rect x="1.5" y="0.75" width="7" height="10.5" rx="1.2" fill="none" stroke="var(--teal)" stroke-width="1.5"/><circle cx="5" cy="9" r="0.8" fill="var(--teal)"/></svg>
        <span>613-4289-517</span>
      </div>
      <div class="contact-line">
        <svg width="12" height="12" viewBox="0 0 12 12" aria-hidden="true"><circle cx="6" cy="6" r="5" fill="none" stroke="var(--teal)" stroke-width="1.4"/><path d="M1 6 H11 M6 1 C3.5 4 3.5 8 6 11 M6 1 C8.5 4 8.5 8 6 11" fill="none" stroke="var(--teal)" stroke-width="1"/></svg>
        <span>www.fyrolume.com</span>
      </div>
    </div>

    <div class="social-band">
      <span class="social-item"><span class="social-item__mark"></span>linkedin -/fyrolum</span>
      <span class="social-item"><span class="social-item__mark"></span>facebook -/fyrolum</span>
      <span class="social-item"><span class="social-item__mark"></span>twitter -/fyrolu</span>
    </div>
  </section>

</main>
</body>
</html>
```